We need a flyer where we promote a workshop to our members of the jewish community www.qvb-gemeinde.example . The workshop is calles "guidance in ten seasons presented by QVB. We would like to see a flyer with the below text is used and also some pictures (attached). The flyer should come over as cool, fresh, innovative for a younger crowd so called young professionals (age 28-35).
TITLE.
"Guidance in Ten Seasons.
SUBTITLE.
Your systematic self-coaching roadmap to power and impact—and your future.”
TEXT.
Dr. Martin K. Halvorsen is the CEO Emeritus of Alpine Advisory Partners—he made an exit in 2013. He is the award-winning author of 8 books, including "Plan-Into-Motion," "Speak or Falter" and "The Cantor and the Chairman.”
For the past 20 years he has taught leadership at Harwick University in New York and at BKU (Lindenberg University) to prepare future CEOs and other leaders in business, government , nonprofits and the military.
Now, in a process exclusively designed for QVB’s next generation of emerging leaders, Martin unpacks his leadership secrets in 3 action-packed labs—reduced to the max:
Lab 1. Guidance in Ten Seasons: The Summit Guide Triangle®. Self-Assessment. Self-Leadership: “The Lantern.” 5-Year Vision. 100-Day Catalytic Project.
Lab 2. Leading Through Language. Relationship: Building Trust. Plan-Into-Motion. Cockpit.
Lab 3. Debrief and Scale-Up. Sustainability. Action Tools.
Do you want to build your own future and a life you love? Do you want to jump-start that future and life over 100 days while learning a toolbox of leadership skills, networking with like-minded people—and even get some pizza? Then join us.
Target Market(s)
young professionals age 28-35

```html
<!DOCTYPE html>
<html lang="en">
<head>
<meta charset="utf-8">
<title>Guidance in Ten Seasons – QVB</title>
<link rel="stylesheet" href="https://fonts.googleapis.com/css2?family=Montserrat:wght@800&family=Oswald:wght@500;600&family=Mulish:wght@400;800&family=PT+Sans+Narrow&family=Open+Sans:wght@400;600;700&display=swap">
<style>
:root{
  --red:#e8411d;
  --dark:#443d4e;
  --grey:#dadada;
  --ink:#2a2a2a;
  --white:#ffffff;
}
*{margin:0;padding:0;box-sizing:border-box}
html,body{width:846px;height:1200px;overflow:hidden;background:#fff}
.flyer{position:relative;width:846px;height:1200px;overflow:hidden;background:var(--white)}
.backdrop{position:absolute;inset:0}
.headline{position:absolute;left:30px;top:22px;font-family:"Montserrat",sans-serif;font-weight:800;font-size:96px;line-height:1;color:var(--white);letter-spacing:1px;white-space:nowrap}
.headline .accent{color:var(--red)}
.brand{position:absolute;left:672px;top:36px;color:var(--white);font-family:"Montserrat",sans-serif;font-weight:800}
.brand-mark{font-size:72px;line-height:1;letter-spacing:-2px}
.brand-name{font-size:15px;line-height:20px;margin-top:8px}
.title-in{position:absolute;left:480px;top:126px;font-family:"Oswald",sans-serif;font-weight:500;font-size:46px;line-height:1;color:var(--red)}
.title-seasons{position:absolute;left:440px;top:180px;font-family:"Oswald",sans-serif;font-weight:500;font-size:70px;line-height:1;color:var(--red);white-space:nowrap}
.subtitle{position:absolute;left:466px;width:320px;top:306px;text-align:center;font-family:"Oswald",sans-serif;font-weight:500;font-size:30px;line-height:35px;color:var(--white);text-transform:uppercase;white-space:nowrap}
.website{position:absolute;left:548px;top:500px;font-family:"Oswald",sans-serif;font-weight:500;font-size:19px;line-height:24px;color:var(--white);white-space:nowrap}
.speaker-name{position:absolute;left:114px;top:544px;font-family:"Oswald",sans-serif;font-weight:600;font-size:23px;color:var(--white);white-space:nowrap}
.bio-box{position:absolute;left:38px;top:732px;width:493px;height:302px;border:3px solid var(--ink);border-radius:3px;background:var(--white);padding:12px 14px 12px;display:flex;flex-direction:column;justify-content:space-between}
.bio{font-family:"PT Sans Narrow",sans-serif;font-size:18px;line-height:23.5px;color:var(--ink);text-align:center}
.bio-lead{font-family:"Open Sans",sans-serif;font-weight:600;font-size:18px;line-height:22px;color:var(--ink);text-align:center}
.bio-lead .accent{color:var(--red)}
.labs{position:absolute;left:557px;width:255px;top:616px;text-align:center;font-family:"Mulish",sans-serif;color:var(--ink)}
.lab{margin-bottom:22px}
.lab h3{font-family:"Mulish",sans-serif;font-weight:800;font-size:31px;line-height:38px;color:var(--red)}
.lab p{font-size:14.5px;line-height:19.5px}
.lab-2{margin-top:14px}
.invite{position:absolute;left:20px;width:510px;top:1064px;text-align:center;font-family:"Open Sans",sans-serif;font-size:15.5px;line-height:25px;color:var(--white)}
.cta{position:absolute;left:523px;top:1068px;width:323px;height:132px;display:flex;align-items:center;justify-content:center;padding-top:16px;font-family:"Open Sans",sans-serif;font-weight:700;font-size:31px;color:var(--white)}
</style>
</head>
<body>
<main class="flyer">
  <svg class="backdrop" width="846" height="1200" viewBox="0 0 846 1200" aria-hidden="true">
    <defs>
      <linearGradient id="portraitTone" x1="0" y1="0" x2="0" y2="1">
        <stop offset="0" stop-color="#d4d4d6"/>
        <stop offset="0.55" stop-color="#b9b7b8"/>
        <stop offset="1" stop-color="#55525a"/>
      </linearGradient>
    </defs>
    <polygon points="0,0 343,0 343,457 474,558 0,728" fill="var(--red)"/>
    <rect x="557" y="520" width="255" height="532" fill="var(--grey)"/>
    <polygon points="343,0 846,0 846,635 343,457" fill="var(--dark)"/>
    <rect x="40" y="138" width="391" height="513" fill="url(#portraitTone)" role="img" aria-label="Portrait photo of Dr. Martin K. Halvorsen"/>
    <polygon points="102,387 398,558 102,726" fill="var(--red)"/>
    <polygon points="203,470 474,558 203,706" fill="none" stroke="var(--red)" stroke-width="6"/>
    <polygon points="606,268 624,268 615,284" fill="#cfcfd4"/>
    <polygon points="768,518 786,528 768,538" fill="#cfcfd4"/>
    <polygon points="531,978 557,1001 531,1024" fill="var(--dark)"/>
    <rect x="0" y="1052" width="846" height="148" fill="var(--dark)"/>
    <rect x="523" y="1068" width="323" height="132" fill="var(--red)"/>
    <polygon points="605,1068 647,1068 626,1098" fill="var(--dark)"/>
  </svg>

  <h1 class="headline">GUIDA<span class="accent">NCE</span></h1>
  <div class="brand">
    <div class="brand-mark">QVB</div>
    <div class="brand-name">Quellenberg<br>Vereinigte<br>Gemeinde</div>
  </div>
  <div class="title-in">IN</div>
  <div class="title-seasons">TEN SEASONS</div>

  <h2 class="subtitle">Your systematic<br>self-coaching<br>roadmap<br>to power and impact<br>—and your future</h2>
  <div class="website">www.qvb-gemeinde.example</div>

  <div class="speaker-name">DR. MARTIN K. HALVORSEN</div>

  <section class="bio-box">
    <p class="bio">Dr. Martin K. Halvorsen is the CEO Emeritus of Alpine Advisory Partners—he made an exit in 2013. He is the award-winning author of 8 books, including "Plan-Into-Motion," "Speak or Falter" and "The Cantor and the Chairman." For the past 20 years he has taught leadership at Harwick University in New York and at BKU (Lindenberg University) to prepare future CEOs and other leaders in business, government, nonprofits and the military.</p>
    <p class="bio-lead">Now, in a process exclusively designed for QVB’s next generation of emerging leaders, Martin unpacks his leadership secrets in <span class="accent">3 action-packed labs</span>—reduced to the max:</p>
  </section>

  <section class="labs">
    <div class="lab lab-1">
      <h3>Lab 1.</h3>
      <p>Guidance in Ten Seasons:<br>The Summit Guide Triangle®.<br>Self-Assessment. Self-Leadership:<br>“The Lantern.”<br>5-Year Vision.<br>100-Day Catalytic Project.</p>
    </div>
    <div class="lab lab-2">
      <h3>Lab 2.</h3>
      <p>Leading Through Language.<br>Relationship: Building Trust.<br>Plan-Into-Motion.<br>Cockpit.</p>
    </div>
    <div class="lab lab-3">
      <h3>Lab 3.</h3>
      <p>Debrief and Scale-Up.<br>Sustainability.<br>Action Tools.</p>
    </div>
  </section>

  <p class="invite">Do you want to build your own future and a life you love? Do you want to jump-start that future and life over 100 days while learning a toolbox of leadership skills, networking with like-minded people—and even get some pizza?</p>
  <div class="cta">THEN JOIN US.</div>
</main>
</body>
</html>
```